Stationery Design Project for Lotvian, Chicago

Lotvian, a street parking application which helps car drivers find a street parking spot by offering an ideal path along which to look for parking. This path is calculated by our algorithm based on data (e.g. historical data, baseball games schedule, etc.). Along this path the driver will find a spot and will also save 70% of the search time. Customer we target is reg. between 21 and 45 yo.

We envision something young, fresh, bright and original. Slightly abstract maybe. It should represent the idea and elements of finding street parking in the city, e.g. car(s), parking spot, people, city, etc. (just ideas!).

Requirement:
- Business Cards (2 Sided Full Color CMYK)
- Letterhead (1 Sided Full Color CMYK)
- Envelope (1 Sided Full Color CMYK)
- Sticker (1 Sided Full Color CMYK), round with a 2inch diameter.

Reason: We're starting to get more and more designs and need more time to look into all of them. Very exciting!! Thanks to everybody!

Hi all, we're in the process of selecting our favs. Though choices!!! Really good submissions. Will keep you posted and sorry for the delay.

Target Market(s)

Car drivers and owners between 21 and 45

Industry/Entity Type

Parking

Requirements
Must have
• Sticker should be round and include company URL lotvian.com and the new logo which we will attach soon.
Should not have
• Should not be too serious or boring.

```html
<!DOCTYPE html>
<html lang="en">
<head>
<meta charset="utf-8">
<title>Lotvian Business Card</title>
<link rel="stylesheet" href="https://fonts.googleapis.com/css2?family=Source+Sans+3:wght@400;600;700&display=swap">
<style>
  :root {
    --page-bg: #e6e7ea;
    --card-white: #ffffff;
    --ink: #1f1f22;
    --ink-soft: #3a3a3e;
    --rule: #4a4a4e;
    --brand-blue: #1f63b8;
    --brand-blue-deep: #2a3f9e;
    --brand-blue-light: #3f86d6;
    --brand-sky: #8fc0f2;
    --band-dark: #2b2b2e;
    --band-grey: #8d8d92;
    --photo-grey: #b9c0c8;
    --photo-blue: #6f8db5;
    --on-blue: #ffffff;
  }
  * { margin: 0; padding: 0; box-sizing: border-box; }
  html, body { width: 996px; height: 1200px; overflow: hidden; }
  body {
    background: var(--page-bg);
    font-family: "Source Sans 3", "Myriad Pro", sans-serif;
    color: var(--ink);
    position: relative;
  }
  .card {
    position: absolute;
    left: 74px;
    width: 802px;
    height: 458px;
    border-radius: 29px;
    overflow: hidden;
    box-shadow: 0 6px 16px rgba(0,0,0,0.25);
  }
  .brand { position: absolute; display: flex; align-items: center; }
  .brand-dot { border-radius: 50%; flex: none; }
  .brand-name { font-weight: 600; letter-spacing: 1px; line-height: 1; }

  /* Front */
  .card-front { top: 134px; background: var(--card-white); }
  .card-front .brand { left: 132px; top: 73px; }
  .card-front .brand-dot { width: 148px; height: 148px; margin-right: 32px; background: var(--brand-blue); }
  .card-front .brand-name { font-size: 104px; color: var(--ink); }

  .holder {
    position: absolute;
    top: 258px; left: 0; right: 0;
    text-align: center;
    font-size: 21px;
    padding-left: 22px;
  }
  .holder-name { font-weight: 700; font-size: 25px; }
  .holder-sep { font-weight: 700; font-size: 25px; margin: 0 2px; }

  .contacts {
    position: absolute;
    top: 330px; left: 46px;
    display: flex;
    font-size: 19.5px;
    line-height: 30px;
    color: var(--ink-soft);
  }
  .contact-group { padding-right: 22px; }
  .contact-group + .contact-group {
    border-left: 1.5px solid var(--rule);
    padding-left: 22px;
  }
  .contact-group b { font-weight: 700; color: var(--ink); }
  .contact-phones { width: 209px; }
  .contact-web { width: 261px; }
  .contact-address { line-height: 27px; padding-top: 5px; }

  .front-band {
    position: absolute;
    left: 0; bottom: 0;
    width: 100%; height: 42px;
    background: linear-gradient(90deg, var(--brand-blue-light), var(--brand-blue) 60%, var(--brand-blue-deep));
  }
  .front-band-dark {
    position: absolute;
    left: 0; top: 0; height: 100%; width: 390px;
    background: linear-gradient(90deg, var(--band-grey) 0%, var(--band-dark) 22%, #111 60%, #333 100%);
    clip-path: polygon(0 0, 360px 0, 390px 100%, 0 100%);
  }

  /* Back */
  .card-back {
    top: 656px;
    background: linear-gradient(90deg, #1f62b6 0%, #2458b2 50%, #2a3f9e 100%);
  }
  .back-ring {
    position: absolute;
    left: 500px; top: 20px;
    width: 390px; height: 390px;
    border-radius: 50%;
    background: rgba(120,150,230,0.16);
  }
  .back-photo {
    position: absolute;
    left: 34px; top: 72px;
    width: 396px; height: 258px;
    background: radial-gradient(ellipse at 45% 45%, var(--photo-grey) 0%, var(--photo-blue) 55%, rgba(31,98,182,0) 80%);
  }
  .card-back .brand { left: 152px; top: 252px; }
  .card-back .brand-dot {
    width: 140px; height: 140px; margin-right: 26px;
    background: var(--brand-sky);
  }
  .card-back .brand-name { font-size: 92px; color: var(--on-blue); }
  .back-contact {
    position: absolute;
    right: 43px; top: 368px;
    font-size: 19.5px;
    color: var(--on-blue);
  }
  .back-contact b { font-weight: 700; }
</style>
</head>
<body>

<section class="card card-front">
  <div class="brand">
    <span class="brand-dot"></span>
    <span class="brand-name">Lotvian</span>
  </div>

  <p class="holder"><span class="holder-name">Your Name</span> <span class="holder-sep">|</span> Designation</p>

  <div class="contacts">
    <div class="contact-group contact-phones">
      <div><b>t</b> : 123-456-7890</div>
      <div><b>m</b> : 123-456-7890</div>
    </div>
    <div class="contact-group contact-web">
      <div><b>e</b> : name@website.com</div>
      <div><b>w</b> : www.website.com</div>
    </div>
    <div class="contact-group contact-address">
      <div>Street Name, City Name</div>
      <div>State Name, Country Code</div>
    </div>
  </div>

  <div class="front-band"><div class="front-band-dark"></div></div>
</section>

<section class="card card-back">
  <div class="back-ring"></div>
  <div class="back-photo" role="img" aria-label="Photo of rows of cars in a parking lot"></div>
  <div class="brand">
    <span class="brand-dot"></span>
    <span class="brand-name">Lotvian</span>
  </div>
  <p class="back-contact"><b>e</b> : name@website.com | <b>w</b> : www.website.com</p>
</section>

</body>
</html>
```